re branding project

We are looking to re brand our entire product range which is made up of a mixture of organic products ( www.brindleoak.eu ) in order to make it more appealing to the main stream market.

The scope of work could include logo change, color or style change and we are also considering the type of packaging that we use.

Attached are design currently in use.

Our aim is to have a united corporate image suitable for a world wide audience across specialists and main stream markets.

The company is growing rapidly and will diversify into other food products areas and they should be part of the design thought process. We want the design to have smart, premium look and feel to it which should be reflected in the packaging used.

This is an idea opportunity for someone to get involved with the award winning market leader in a long term projects.

Target Market(s)

people who are passionate about their food and healthy life style, educated, health conscious, high disposable income, families with kids where family health is important, sports people, diet conscious, gluten free market, dairy free, sugar free snack option

Industry/Entity Type

It Company

Requirements
Must have
• appeal to mass market
Should not have
• the design should not only appeal to vegans and organic foodists

```html
<!DOCTYPE html>
<html lang="en">
<head>
<meta charset="utf-8">
<title>Brindleoak – Brazil Nut and Thyme Raw Crackers</title>
<link rel="stylesheet" href="https://fonts.googleapis.com/css2?family=Open+Sans:wght@600&family=Reenie+Beanie&family=Lora:wght@500&display=swap">
<style>
  :root {
    --backdrop: #ffffff;
    --pack-black: #1e1e1e;
    --brand-white: #ffffff;
    --cracker-deep: #8a5426;
    --cracker-mid: #b97c44;
    --cracker-light: #d2a06a;
    --label-beige: #cdc6b6;
    --label-beige-light: #d8d2c4;
    --ink-dark: #2a2622;
    --accent-red: #b8262a;
    --badge-cream: #efe7d6;
    --eu-green: #7fae3c;
  }
  * { margin: 0; padding: 0; box-sizing: border-box; }
  html, body {
    width: 845px;
    height: 1200px;
    overflow: hidden;
    background: var(--backdrop);
  }
  .canvas {
    position: relative;
    width: 845px;
    height: 1200px;
    background: var(--backdrop);
  }
  .pack-front {
    position: absolute;
    left: 142px;
    top: 40px;
    width: 560px;
    height: 1120px;
    overflow: hidden;
    box-shadow: 0 18px 40px rgba(0,0,0,0.12);
  }
  .pack-top {
    position: absolute;
    left: 0; top: 0;
    width: 100%;
    height: 350px;
    background: var(--pack-black);
  }
  .brand-name {
    position: absolute;
    left: 0; right: 0;
    top: 186px;
    text-align: center;
    font-family: "Open Sans", sans-serif;
    font-weight: 600;
    font-size: 50px;
    letter-spacing: -0.5px;
    color: var(--brand-white);
  }
  .product-photo {
    position: absolute;
    left: 0; top: 350px;
    width: 100%;
    height: 385px;
    background: linear-gradient(100deg, var(--cracker-light) 0%, var(--cracker-mid) 35%, var(--cracker-deep) 60%, var(--cracker-mid) 80%, var(--cracker-light) 100%);
  }
  .colour-band {
    position: absolute;
    left: 0; top: 735px;
    width: 100%;
    height: 14px;
    background: linear-gradient(90deg, #c8302c, #e7a21f, #7fae3c, #c8302c, #e7a21f, #7fae3c, #c8302c);
  }
  .label-panel {
    position: absolute;
    left: 0; top: 749px;
    width: 100%;
    height: 371px;
    background: linear-gradient(180deg, var(--label-beige-light), var(--label-beige));
  }
  .organic-badge {
    position: absolute;
    right: 18px;
    top: 598px;
  }
  .eu-mark {
    position: absolute;
    left: 20px;
    top: 770px;
  }
  .flavour-name {
    position: absolute;
    left: 0; right: 0;
    top: 838px;
    text-align: center;
    font-family: "Reenie Beanie", cursive;
    font-size: 82px;
    line-height: 0.82;
    color: var(--ink-dark);
  }
  .product-type {
    position: absolute;
    left: 0; right: 0;
    top: 1030px;
    text-align: center;
    font-family: "Lora", serif;
    font-weight: 500;
    font-size: 22px;
    letter-spacing: 1px;
    color: var(--accent-red);
  }
</style>
</head>
<body>
  <main class="canvas">
    <section class="pack-front">
      <div class="pack-top">
        <div class="brand-name">brindleoak</div>
      </div>

      <div class="product-photo" role="img" aria-label="Close-up photograph of stacked brazil nut and thyme raw crackers"></div>

      <div class="colour-band" role="img" aria-label="Decorative multicoloured dashed stripe"></div>

      <div class="label-panel"></div>

      <svg class="organic-badge" width="118" height="118" viewBox="0 0 118 118" aria-hidden="true">
        <circle cx="59" cy="59" r="57" fill="var(--badge-cream)" fill-opacity="0.85"/>
      </svg>

      <svg class="eu-mark" width="44" height="62" viewBox="0 0 44 62" aria-hidden="true">
        <rect x="0" y="0" width="44" height="62" fill="var(--eu-green)"/>
      </svg>

      <h1 class="flavour-name">Brazil Nut<br>and Thyme</h1>
      <p class="product-type">RAW CRACKERS</p>
    </section>
  </main>
</body>
</html>
```